Website of KESTRAVO | The Amber Horizon Company

I need a simple and effective website where users can quickly understand what the company is all about and the added value of the services provided. The site should be attractive and modern, based on the logo and on the corporate slideshow attached.

Target Market(s)

Public and Private organizations from maritime security and defense, looking for solutions in the field s of digital transformation and cybersecurity.

Coding

Coded - Design and coding required

Requirements
Must have
• A form through which can contact the company by email to request additional information.

```html
<!DOCTYPE html>
<html lang="en">
<head>
<meta charset="utf-8">
<title>KESTRAVO | The Amber Horizon Company</title>
<link href="https://fonts.googleapis.com/css2?family=Raleway:wght@400;600;700;800&family=Poppins:wght@400;500;600&display=swap" rel="stylesheet">
<style>
:root{
  --blue:#2a97d8;
  --blue-deep:#1a6fa9;
  --navy:#0b2a44;
  --ink:#111418;
  --sky:#e5f3fc;
  --white:#ffffff;
  --grey:#555b63;
}
*{box-sizing:border-box;margin:0;padding:0}
html,body{width:1200px;height:5029px;overflow:hidden;background:var(--white)}
body{position:relative;font-family:"Poppins",sans-serif;color:var(--ink)}
.abs{position:absolute}
.head-font{font-family:"Raleway",sans-serif}

/* header */
.site-header{left:0;top:0;width:1200px;height:129px;background:var(--white)}
.brand{left:68px;top:30px;display:flex;align-items:center;gap:14px}
.brand-mark{width:52px;height:52px;background:var(--blue);border-radius:8px}
.brand-name{font-family:"Raleway",sans-serif;font-weight:700;font-size:40px;line-height:1;color:var(--ink)}
.brand-tag{font-family:"Raleway",sans-serif;font-weight:700;font-size:12px;letter-spacing:5px;color:var(--ink);margin-top:4px}
.nav{left:545px;top:62px;display:flex;gap:0;font-size:12px;color:var(--ink)}
.nav a{color:inherit;text-decoration:none;margin-right:40px}
.nav a.active{color:var(--blue)}
.btn-pill{left:988px;top:45px;width:147px;height:49px;border-radius:25px;background:var(--blue);color:var(--white);font-weight:600;font-size:13px;display:flex;align-items:center;justify-content:center}

/* hero */
.hero-photo{left:0;top:129px;width:1200px;height:830px;background:radial-gradient(ellipse at 30% 40%,#2f9bcf 0%,#1777b5 45%,#0c4e86 100%)}
.hero-panel{left:486px;top:230px;width:636px;height:515px;border-radius:40px;background:rgba(30,110,170,.55)}
.hero-title{left:486px;top:285px;width:636px;text-align:center;color:var(--white);font-family:"Raleway",sans-serif;line-height:1.12}
.hero-title .strong{font-weight:800;font-size:66px;display:block}
.hero-title .light{font-weight:500;font-size:57px;display:block}
.btn-offset{display:flex;align-items:center;justify-content:center;background:var(--blue);color:var(--white);font-weight:500;border-radius:14px 0 14px 0;box-shadow:-6px -6px 0 var(--navy)}
.hero-btn{left:698px;top:610px;width:217px;height:70px;font-size:22px}
.dots{left:572px;top:830px;display:flex;gap:5px}
.dots span{width:11px;height:11px;border-radius:50%;background:rgba(255,255,255,.55)}
.dots span:first-child{background:var(--white)}

/* section heads */
.sec-mark{width:42px;height:42px;background:var(--blue);border-radius:6px}
.sec-title{font-family:"Raleway",sans-serif;font-weight:700;font-size:47px;line-height:1}
.sec-title .hi{color:var(--blue-deep)}
.sec-title .lo{color:var(--navy)}

/* service cards */
.card{width:511px;height:429px;border-radius:0 60px 0 80px;border-top:12px solid var(--blue);border-left:12px solid var(--blue)}
.card.dark{border-color:var(--ink)}
.card-photo{position:absolute;left:0;top:0;right:0;bottom:0;border-radius:0 50px 0 70px}
.card-label{position:absolute;right:-16px;bottom:-1px;width:430px;height:78px;background:var(--white);border-radius:55px 0 0 0;font-family:"Raleway",sans-serif;font-weight:700;font-size:28px;padding:26px 0 0 30px}

/* why choose */
.why{left:0;top:1787px;width:1200px;height:663px;background:var(--sky)}
.feat-label{font-size:16px;font-weight:600;color:var(--ink)}
.feat-icon{width:116px;height:116px;border-radius:50%;border:2px dotted var(--blue-deep);display:flex;align-items:center;justify-content:center}
.feat-icon .core{width:100px;height:100px;border-radius:50%;background:radial-gradient(circle at 35% 30%,#2a8cc9,#06233d 75%);display:flex;align-items:center;justify-content:center}

/* about */
.frame{border-top:12px solid var(--blue);border-left:12px solid var(--blue);border-radius:0 60px 0 80px}
.about-text{font-size:13.5px;line-height:26px;color:var(--grey);text-align:justify}
.btn-small{font-size:15px}

/* collaborate */
.collab{left:0;top:3166px;width:1200px;height:615px;background:linear-gradient(180deg,#0c1c2b 0%,#0a2234 55%,#0d2c44 100%)}

/* form */
.field{background:var(--white);box-shadow:0 2px 10px rgba(0,0,0,.12);font-size:11px;color:#8a8f96;padding:14px 18px}

/* footer */
.footer-bg{left:0;top:4487px;width:1200px;height:470px}
.foot-head{font-family:"Raleway",sans-serif;font-weight:700;font-size:22px;color:var(--white)}
.foot-rule{width:46px;height:3px;background:var(--white);margin-top:8px}
.foot-link{font-size:13px;color:var(--white);display:flex;align-items:center;gap:14px}
.foot-icon{width:38px;height:38px;border:1.5px solid rgba(255,255,255,.7);border-radius:6px;display:flex;align-items:center;justify-content:center}
.copyright{left:0;top:4955px;width:1200px;height:74px;background:#0a0d10;color:var(--white);font-size:11px;display:flex;align-items:center;justify-content:center}
</style>
</head>
<body>

<!-- header -->
<header class="site-header abs">
  <div class="brand abs">
    <div class="brand-mark"></div>
    <div>
      <div class="brand-name">KESTRAVO</div>
      <div class="brand-tag">AMBER HORIZON</div>
    </div>
  </div>
  <nav class="nav abs">
    <a class="active">HOME</a><a>ABOUT US</a><a>SERVICES</a><a>WHY CHOOSE US</a>
  </nav>
  <div class="btn-pill abs">CONTACT US</div>
</header>

<!-- hero -->
<section>
  <div class="hero-photo abs" role="img" aria-label="Aerial view of a loaded container ship sailing on deep blue sea"></div>
  <svg class="abs" style="left:0;top:820px" width="1200" height="150" viewBox="0 0 1200 150">
    <path d="M0 20 Q600 200 1200 20 L1200 150 L0 150 Z" fill="#1d86c8"/>
    <path d="M0 48 Q600 215 1200 30 L1200 150 L0 150 Z" fill="#ffffff"/>
  </svg>
  <div class="hero-panel abs"></div>
  <h1 class="hero-title abs">
    <span class="strong">INNOVATIVE</span>
    <span class="strong">SOLUTIONS FOR</span>
    <span class="light">MARITIME SECURITY</span>
    <span class="light">AND DEFENSE</span>
  </h1>
  <div class="hero-btn btn-offset abs">CONTACT US</div>
  <div class="dots abs"><span></span><span></span><span></span><span></span></div>
</section>

<!-- services -->
<section>
  <div class="sec-mark abs" style="left:579px;top:1066px"></div>
  <h2 class="sec-title abs" style="left:0;top:1125px;width:1200px;text-align:center"><span class="hi">OUR</span> <span class="lo">SERVICES</span></h2>

  <div class="card abs" style="left:68px;top:1233px">
    <div class="card-photo" style="background:linear-gradient(135deg,#e9eef1,#c9d2d8 55%,#8b949c)" role="img" aria-label="Two colleagues working together at a laptop in a bright office"></div>
    <div class="card-label" style="color:var(--blue-deep)">STRATEGY AND DESIGN</div>
  </div>
  <div class="card dark abs" style="left:622px;top:1233px">
    <div class="card-photo" style="background:linear-gradient(135deg,#3b2b22,#7d6a5d 45%,#e3e8ec)" role="img" aria-label="Hand signing a document with a pen at a desk"></div>
    <div class="card-label" style="color:var(--ink)">EXECUTION AND DELIVERY</div>
  </div>
</section>

<!-- why choose us -->
<section class="why abs">
  <div class="sec-mark abs" style="left:579px;top:85px"></div>
  <h2 class="sec-title abs" style="left:0;top:145px;width:1200px;text-align:center"><span class="hi">WHY CHOOSE</span> <span class="lo">US ?</span></h2>

  <svg class="abs" style="left:300px;top:290px" width="600" height="300" viewBox="0 0 600 300">
    <defs>
      <linearGradient id="dome" x1="0" y1="0" x2="1" y2="1">
        <stop offset="0" stop-color="#1b80bf"/><stop offset="1" stop-color="#04121f"/>
      </linearGradient>
    </defs>
    <path d="M15 292 A285 285 0 0 1 585 292" fill="none" stroke="#1a6fa9" stroke-width="1.5" stroke-dasharray="2 4"/>
    <path d="M38 292 A262 262 0 0 1 562 292 Z" fill="url(#dome)"/>
    <circle cx="116" cy="98" r="8" fill="#2a97d8"/>
    <circle cx="502" cy="100" r="8" fill="#2a97d8"/>
    <circle cx="27" cy="232" r="8" fill="#2a97d8"/>
    <circle cx="588" cy="234" r="8" fill="#2a97d8"/>
  </svg>

  <div class="feat-label abs" style="left:130px;top:293px;width:126px;text-align:right">Expert Team</div>
  <div class="feat-icon abs" style="left:276px;top:246px"><div class="core">
    <svg width="50" height="40" viewBox="0 0 50 40" fill="#fff"><circle cx="25" cy="10" r="7"/><circle cx="11" cy="14" r="5"/><circle cx="39" cy="14" r="5"/><path d="M13 36 Q25 14 37 36Z"/><path d="M2 34 Q10 20 18 30Z"/><path d="M32 30 Q40 20 48 34Z"/></svg>
  </div></div>

  <div class="feat-label abs" style="left:968px;top:295px">Proven Partnerships</div>
  <div class="feat-icon abs" style="left:832px;top:248px"><div class="core">
    <svg width="46" height="46" viewBox="0 0 46 46" fill="none" stroke="#fff" stroke-width="4" stroke-linecap="round" stroke-linejoin="round"><path d="M6 24 L18 12 L28 18 L40 8"/><path d="M10 30 L22 40 L38 24"/></svg>
  </div></div>

  <div class="feat-label abs" style="left:68px;top:421px">Tailored Strategies</div>
  <div class="feat-icon abs" style="left:156px;top:461px"><div class="core">
    <svg width="48" height="48" viewBox="0 0 48 48" fill="none" stroke="#fff" stroke-width="3.5"><circle cx="22" cy="26" r="17"/><circle cx="22" cy="26" r="9"/><circle cx="22" cy="26" r="2" fill="#fff"/><path d="M22 26 L42 6 M36 6 H42 V12" stroke-linecap="round"/></svg>
  </div></div>

  <div class="feat-label abs" style="left:930px;top:425px;width:212px;text-align:right">Innovative Solutions</div>
  <div class="feat-icon abs" style="left:942px;top:463px"><div class="core">
    <svg width="46" height="46" viewBox="0 0 46 46" fill="#fff"><circle cx="23" cy="20" r="9"/><rect x="18" y="28" width="10" height="8" rx="2"/><g stroke="#fff" stroke-width="3" stroke-linecap="round"><path d="M23 2 V6 M8 20 H4 M42 20 H38 M11 8 L14 11 M35 8 L32 11"/></g></svg>
  </div></div>
</section>

<!-- about -->
<section>
  <div class="frame abs" style="left:88px;top:2567px;width:548px;height:461px">
    <div class="abs" style="left:0;top:0;right:0;bottom:0;border-radius:0 50px 0 70px;background:linear-gradient(135deg,#f3f1ec,#dcd8d0 50%,#2b3a55)" role="img" aria-label="Four business professionals standing together in an office"></div>
  </div>
  <div class="sec-mark abs" style="left:720px;top:2593px"></div>
  <h2 class="sec-title abs" style="left:720px;top:2643px;color:var(--ink)">ABOUT US</h2>
  <p class="about-text abs" style="left:720px;top:2719px;width:387px">KESTRAVO specializes in delivering innovative solutions for maritime security and defense in the fields of digital transformation and cybersecurity.</p>
  <p class="about-text abs" style="left:720px;top:2826px;width:387px">By combining unparalleled expertise with strategic partnerships, we empower organizations to overcome challenges, seize opportunities, and achieve success.</p>
  <div class="btn-offset btn-small abs" style="left:728px;top:2945px;width:157px;height:41px">READ MORE</div>
</section>

<!-- collaborate -->
<section class="collab abs" role="img" aria-label="Dark harbour scene with cargo cranes at dusk">
  <div class="sec-mark abs" style="left:579px;top:90px"></div>
  <h2 class="sec-title abs" style="left:0;top:146px;width:1200px;text-align:center;color:var(--blue)">LET'S COLLABORATE</h2>
  <h3 class="abs head-font" style="left:0;top:250px;width:1200px;text-align:center;color:var(--white);font-weight:700;font-size:41px">Ready to innovate together?</h3>
  <p class="abs" style="left:130px;top:337px;width:940px;text-align:center;color:var(--white);font-size:19.5px;line-height:38px">KESTRAVO is here to help you navigate challenges and unlock new opportunities for maritime security and defense with digital transformation and cybersecurity solutions.</p>
  <div class="btn-offset abs" style="left:492px;top:459px;width:218px;height:62px;font-size:21px;font-weight:600;box-shadow:-6px -6px 0 #ffffff">CONTACT US</div>
</section>

<!-- contact -->
<section>
  <div class="sec-mark abs" style="left:105px;top:3898px"></div>
  <h2 class="sec-title abs" style="left:105px;top:3948px;color:var(--ink)">CONTACT US</h2>
  <div class="field abs" style="left:104px;top:4043px;width:196px;height:37px">First Name:</div>
  <div class="field abs" style="left:320px;top:4043px;width:197px;height:37px">Last Name:</div>
  <div class="field abs" style="left:104px;top:4100px;width:196px;height:38px">Phone:</div>
  <div class="field abs" style="left:320px;top:4100px;width:197px;height:38px">Email:</div>
  <div class="field abs" style="left:104px;top:4162px;width:413px;height:125px">Message:</div>
  <div class="btn-offset abs" style="left:107px;top:4330px;width:164px;height:43px;font-size:15px">SUBMIT NOW</div>

  <div class="frame abs" style="left:602px;top:3902px;width:495px;height:460px">
    <div class="abs" style="left:0;top:0;right:0;bottom:0;border-radius:0 50px 0 70px;background:linear-gradient(135deg,#eef0f2,#b9c2cb 50%,#2c3440)" role="img" aria-label="Team of colleagues collaborating around a computer"></div>
  </div>
</section>

<!-- footer -->
<footer>
  <svg class="footer-bg abs" width="1200" height="470" viewBox="0 0 1200 470">
    <defs>
      <linearGradient id="footfill" x1="0" y1="0" x2="0" y2="1">
        <stop offset="0" stop-color="#1f7cbc"/><stop offset="1" stop-color="#165d92"/>
      </linearGradient>
    </defs>
    <path d="M0 110 Q600 -70 1200 110 L1200 470 L0 470 Z" fill="#2a97d8"/>
    <path d="M0 125 Q600 -35 1200 125 L1200 470 L0 470 Z" fill="#ffffff"/>
    <path d="M0 140 Q600 -20 1200 140 L1200 470 L0 470 Z" fill="url(#footfill)"/>
  </svg>

  <div class="abs head-font" style="left:74px;top:4748px;width:316px;text-align:center;color:var(--white);font-weight:600;font-size:62px;line-height:1">KESTRAVO</div>
  <div class="abs head-font" style="left:74px;top:4822px;width:316px;text-align:center;color:var(--white);font-weight:600;font-size:19px;letter-spacing:9px">AMBER HORIZON</div>

  <div class="abs" style="left:474px;top:4644px">
    <div class="foot-head">Quick Links</div><div class="foot-rule"></div>
  </div>
  <div class="abs" style="left:478px;top:4740px;display:flex;flex-direction:column;gap:21px">
    <div class="foot-link">›&nbsp;About Us</div>
    <div class="foot-link">›&nbsp;Services</div>
    <div class="foot-link">›&nbsp;Why Choose Us?</div>
    <div class="foot-link">›&nbsp;Contact Us</div>
  </div>

  <div class="abs" style="left:696px;top:4644px">
    <div class="foot-head">Contact Us</div><div class="foot-rule"></div>
  </div>
  <div class="abs" style="left:696px;top:4736px;display:flex;flex-direction:column;gap:22px">
    <div class="foot-link"><div class="foot-icon"><svg width="16" height="16" viewBox="0 0 16 16" fill="none" stroke="#fff" stroke-width="1.6"><path d="M3 1 L6 1 L7 5 L5 6 Q6 9 10 11 L11 9 L15 10 L15 13 Q14 15 12 15 Q2 13 1 3 Q1 1 3 1Z"/></svg></div><div style="font-size:11.5px;line-height:18px">CALL US<br>555 014 2290</div></div>
    <div class="foot-link"><div class="foot-icon"><svg width="18" height="14" viewBox="0 0 18 14" fill="none" stroke="#fff" stroke-width="1.6"><rect x="1" y="1" width="16" height="12" rx="1"/><path d="M1 2 L9 8 L17 2"/></svg></div><div style="font-size:11.5px;line-height:18px">EMAIL US<br>office@kestravo.com</div></div>
    <div class="foot-link"><div class="foot-icon"><svg width="18" height="18" viewBox="0 0 18 18" fill="none" stroke="#fff" stroke-width="1.5"><circle cx="9" cy="9" r="7.5"/><ellipse cx="9" cy="9" rx="3.5" ry="7.5"/><path d="M1.5 9 H16.5"/></svg></div><div style="font-size:11.5px;line-height:18px">WEBSITE<br>www.kestravo.com</div></div>
  </div>

  <div class="abs" style="left:975px;top:4642px">
    <div class="foot-head">Follow Us</div><div class="foot-rule"></div>
  </div>
  <div class="abs" style="left:977px;top:4738px;display:flex;flex-direction:column;gap:22px">
    <div class="foot-link" style="font-size:16px"><div class="foot-icon"></div>COMMUNITY</div>
    <div class="foot-link" style="font-size:16px"><div class="foot-icon"></div>UPDATES</div>
    <div class="foot-link" style="font-size:16px"><div class="foot-icon"></div>GALLERY</div>
  </div>

  <div class="copyright abs">Copyright © 2025 All Rights Reserved By Company name</div>
</footer>

</body>
</html>
```